Locksmiths Business Card Designs needed!!

I need a business card design for my new small locksmith business.
I would love my business card to be simple, (not too many photos of locks or keys) but strong images so that everyone can recognise it is locksmithing business without reading the words.

I want all information i put in upper article to appear on front side in anyway depending on your design of suggestions and on the back side I would love to mention theses;
-24 /7 mobile services (including weekends & public holidays)
-Residential / Commercial/ Automotive
-Opening / Repair / Installation
-Cut keys

Im not a native english speaker so you can fix the words or expressions as you think it is right and natural.

I realised that in the business names, there is too many "locks" and "s" so I would love to seperate the words somehow so that it is more natural when someone read the business name on the card. for example,put the part of "Bright Harbor Access" first line and the part of "Locksmiths" on the other line....I am just suggesting..doesn't need to be like that..but it should say "Locksmiths" as it is locksmiths business. :)

Target Market(s)

all generations

Industry/Entity Type

Locksmith

Contact Information for Business Card

business name : Bright Harbor Access Services
ABN 41862093715
Name : Dean Rowe (푸른 문지기)
phone : 0468 219 357
email : brightharboraccess@mailverte.net

Requirements
Must have
• A symbol of either a key or a lock
Nice to have
• I like the symbol of a key in the photo I have attached here. So maybe, if you couldn't find any other good symbols I am happy to have the symbol on the business somehow.
Should not have
• Too many keys or locks

```html
<!DOCTYPE html>
<html lang="en">
<head>
<meta charset="utf-8">
<title>Bright Harbor Access Locksmiths – Business Card</title>
<link rel="stylesheet" href="https://fonts.googleapis.com/css2?family=PT+Sans:ital,wght@0,700;1,700&display=swap">
<style>
  :root {
    --card-bg: #363636;
    --brand-blue: #00aeef;
    --ink-white: #ffffff;
  }
  * { margin: 0; padding: 0; box-sizing: border-box; }
  html, body {
    width: 1200px;
    height: 693px;
    overflow: hidden;
    background: var(--card-bg);
  }
  .card {
    position: relative;
    width: 1200px;
    height: 693px;
    background: var(--card-bg);
    font-family: "PT Sans", Arial, sans-serif;
    color: var(--ink-white);
    overflow: hidden;
  }
  .brand-mark {
    position: absolute;
    left: 74px;
    top: 86px;
    width: 124px;
    height: 124px;
    border-radius: 50%;
    background: var(--ink-white);
  }
  .brand-name {
    position: absolute;
    left: 218px;
    top: 78px;
    font-weight: 700;
    font-style: normal;
    font-size: 42px;
    line-height: 46px;
    color: var(--ink-white);
    white-space: nowrap;
  }
  .services {
    position: absolute;
    left: 72px;
    top: 318px;
    list-style: none;
  }
  .services li {
    position: relative;
    padding-left: 30px;
    font-weight: 700;
    font-style: italic;
    font-size: 38px;
    line-height: 45px;
    letter-spacing: -0.2px;
    white-space: nowrap;
  }
  .services li::before {
    content: "";
    position: absolute;
    left: 0;
    top: 17px;
    width: 11px;
    height: 11px;
    border-radius: 50%;
    background: var(--brand-blue);
  }
  .services .lead-item { padding-left: 36px; }
  .bands {
    position: absolute;
    left: 0;
    top: 0;
  }
  .band-blue { fill: var(--brand-blue); }
  .band-white { fill: var(--ink-white); }
</style>
</head>
<body>
  <div class="card">
    <span class="brand-mark"></span>
    <div class="brand-name">Bright Harbor Access<br>Locksmiths</div>

    <ul class="services">
      <li class="lead-item">All suburbs</li>
      <li>24 /7 mobile services (including weekends &amp; public holidays)</li>
      <li>Residential / Commercial/ Automotive</li>
      <li>Opening / Repair / Installation</li>
      <li>Cut keys</li>
    </ul>

    <svg class="bands" width="1200" height="693" viewBox="0 0 1200 693" aria-hidden="true">
      <polygon class="band-blue" points="0,579 802,579 772,630 0,630"/>
      <polygon class="band-white" points="806,589 1200,589 1200,647 768,647"/>
    </svg>
  </div>
</body>
</html>
```